Business Card for Freelance Copywriting & Web Design Business

Hi! I have a logo but want a new business card. Here's a better idea of what I'm thinking:
-Brand new double-sided business card, rounded cards, embossed logo, nice quality paper
-Include phone (604-382-5194), email (hello@lauraberndt.org), and website (www.lauraberndt.org). No address, please, since I service clients worldwide.
-I'd like the fonts to match those on my website (www.lauraberndt.org). I had to purchase the one font (Born Ready), attached. I'm not sure which version was used on my site so I included all that I purchased. The secondary font is Helvetica
-I'd also like the tagline "Powerful Words. Impressive Results." included.
-My primary brand colour is the teal, colour #19ADC3
Laura Berndt | Laura Berndt Copywriting & Web Design <hello@lauraberndt.org>
-I'd also like the following services listed on the new cards:
SEO Website Content
SEO Blog Content
SEO Website Design
Contact Information for Business Card
as stated in brief
Font styles to use
Other font styles liked:
- See brief
Look and feel
Each slider illustrates characteristics of the customer's brand and the style your logo design should communicate.

```html
<!DOCTYPE html>
<html lang="en">
<head>
<meta charset="utf-8">
<title>Laura Berndt Copywriting &amp; Web Design – Business Card</title>
<link rel="stylesheet" href="https://fonts.googleapis.com/css2?family=Montserrat:wght@400;600;700&display=swap">
<style>
  :root {
    --backdrop: #2e2f31;
    --card: #f7f7f7;
    --card-shade: #ececec;
    --teal-deep: #5b9aa1;
    --teal-mid: #6fb0ba;
    --teal-light: #a7d3dc;
    --ink: #1c1c1c;
    --grey: #5c5c5c;
    --rule: #8a8a8a;
  }
  * { box-sizing: border-box; margin: 0; padding: 0; }
  html, body {
    width: 1200px; height: 900px; overflow: hidden;
    background: var(--backdrop);
    font-family: "Montserrat", Helvetica, Arial, sans-serif;
  }
  .canvas { position: relative; width: 1200px; height: 900px; }

  .card {
    position: absolute; left: 280px; width: 640px; height: 366px;
    border-radius: 30px; overflow: hidden;
    background: linear-gradient(135deg, #ffffff 0%, var(--card) 55%, var(--card-shade) 100%);
    box-shadow: 0 18px 40px rgba(0,0,0,.45);
  }
  .card--front { top: 58px; }
  .card--back { top: 476px; }

  .band { position: absolute; top: 0; height: 100%; }
  .band--left { left: 0; width: 200px; }
  .band--right { right: 0; width: 270px; }

  .feather {
    position: absolute;
    border-radius: 50% 50% 45% 55% / 60% 60% 40% 40%;
    background: radial-gradient(ellipse at 50% 40%, var(--teal-light) 0%, var(--teal-mid) 60%, rgba(111,176,186,0) 100%);
    opacity: .9;
  }
  .card--front .feather { left: 60px; top: 30px; width: 170px; height: 310px; transform: rotate(-20deg); }
  .card--back .feather { left: 380px; top: 20px; width: 200px; height: 320px; transform: rotate(-55deg); }

  .brand { position: absolute; color: var(--ink); font-weight: 600; }
  .brand__name { font-size: 34px; line-height: 1; letter-spacing: .5px; }
  .brand__line { font-size: 11px; letter-spacing: 2.5px; text-transform: uppercase; margin-top: 8px; }
  .card--front .brand { left: 340px; top: 92px; }
  .card--back .brand { left: 44px; top: 84px; }

  .services { position: absolute; left: 380px; top: 180px; }
  .services__title { font-size: 22px; color: var(--teal-mid); font-weight: 400; margin-bottom: 8px; }
  .services__list { list-style: none; color: var(--grey); font-size: 16px; line-height: 1.35; }

  .contact { position: absolute; left: 44px; top: 208px; list-style: none; }
  .contact__item { display: flex; align-items: center; gap: 12px; font-size: 16px; color: var(--grey); line-height: 1.6; }
  .contact__icon { width: 16px; height: 16px; fill: none; stroke: var(--teal-mid); stroke-width: 1.8; }

  .rule { position: absolute; left: 44px; top: 306px; width: 360px; border-top: 1px solid var(--rule); }
  .tagline { position: absolute; left: 44px; top: 318px; font-size: 18px; font-weight: 700; color: var(--teal-mid); letter-spacing: .3px; }
</style>
</head>
<body>
<main class="canvas">

  <section class="card card--front" aria-label="Card front">
    <svg class="band band--left" viewBox="0 0 200 366" preserveAspectRatio="none" aria-hidden="true">
      <path d="M0 0 H60 C110 90 150 200 200 366 H0 Z" fill="var(--teal-deep)"/>
    </svg>
    <div class="feather" role="img" aria-label="Large light teal feather illustration"></div>
    <div class="brand">
      <div class="brand__name">Laura Berndt</div>
      <div class="brand__line">Copywriting &amp; Web Design</div>
    </div>
    <div class="services">
      <h2 class="services__title">Services</h2>
      <ul class="services__list">
        <li>SEO Website Content</li>
        <li>SEO Blog Content</li>
        <li>SEO Website Design</li>
      </ul>
    </div>
  </section>

  <section class="card card--back" aria-label="Card back">
    <svg class="band band--right" viewBox="0 0 270 366" preserveAspectRatio="none" aria-hidden="true">
      <path d="M0 0 H270 V366 H200 C180 220 120 90 0 0 Z" fill="var(--teal-deep)"/>
    </svg>
    <div class="feather" role="img" aria-label="Large light teal feather illustration"></div>
    <div class="brand">
      <div class="brand__name">Laura Berndt</div>
      <div class="brand__line">Copywriting &amp; Web Design</div>
    </div>
    <ul class="contact">
      <li class="contact__item">
        <svg class="contact__icon" viewBox="0 0 16 16" aria-hidden="true"><path d="M3 1.5l2.5 0 1 3.5-1.6 1.2c.8 1.8 2.1 3.1 3.9 3.9L10 8.5l3.5 1v2.5c0 1-1 2-2 2C6 14 2 10 2 4.5c0-1 .5-3 1-3z"/></svg>
        <span>604-382-5194</span>
      </li>
      <li class="contact__item">
        <svg class="contact__icon" viewBox="0 0 16 16" aria-hidden="true"><rect x="1.5" y="3.5" width="13" height="9"/><path d="M1.5 3.5l6.5 5 6.5-5"/></svg>
        <span>hello@lauraberndt.org</span>
      </li>
      <li class="contact__item">
        <svg class="contact__icon" viewBox="0 0 16 16" aria-hidden="true"><circle cx="8" cy="8" r="6.5"/><ellipse cx="8" cy="8" rx="3" ry="6.5"/><path d="M1.5 8h13"/></svg>
        <span>www.lauraberndt.org</span>
      </li>
    </ul>
    <div class="rule" aria-hidden="true"></div>
    <p class="tagline">Powerful Words. Impressive Results.</p>
  </section>

</main>
</body>
</html>
```